New Baby Formula Company Needs a Shopify Website Design

We are launching a baby formula company and need a Shopify website design. We have a patented product that is a disposable pouch with a frangible seal through the middle. The top half contains formula powder and the bottom half contains purified water. There is also a bottle nipple on the corner under the cap in order to feed the baby. You just need to squeeze the bottom half of the pouch to break the seal and then the water and formula will mix. You then only need to shake it and then remove the cap and feed the baby. We will also sell formula in containers like the other formula companies. We want this website to stand out and look professional. We don't want a boring layout, but something unique and captivating. I have attached a mockup rendering of our product, though it's not the finished product and our logo. This will let you know the color scheme we are going for. Let me know if you have any further questions. Thank you

```html
<!DOCTYPE html>
<html lang="en">
<head>
<meta charset="utf-8">
<title>Pipkin – Perfect Baby Feed</title>
<link href="https://fonts.googleapis.com/css2?family=Kalam:wght@400;700&family=Poppins:wght@400;500;600&display=swap" rel="stylesheet">
<style>
:root{
  --brown:#8a5a1c;
  --rust:#9a5a26;
  --olive:#8db52e;
  --leaf:#94cc80;
  --beige:#f8deb0;
  --cream:#fefbe6;
  --ink:#1d1d1b;
  --muted:#6d6d66;
  --footer:#585d54;
  --white:#ffffff;
}
*{margin:0;padding:0;box-sizing:border-box}
html,body{width:1200px;height:4476px;overflow:hidden}
body{position:relative;font-family:"Poppins",sans-serif;color:var(--ink);background:var(--white)}
.abs{position:absolute}
.display{font-family:"Kalam",cursive;font-weight:700;line-height:1.05}
.btn{position:absolute;display:flex;align-items:center;justify-content:center;gap:10px;border-radius:30px;font-family:"Kalam",cursive;font-weight:700;font-size:16px;color:var(--white);background:var(--olive)}
.btn-outline{background:var(--white);border:2px solid #e0c8a8;color:var(--rust)}
.underline{position:absolute;height:5px;width:70px;border-radius:3px;background:var(--olive)}
.media{position:absolute}
.topbar{left:0;top:0;width:1200px;height:30px;background:var(--brown);color:#fff;font-size:11px;display:flex;align-items:center;justify-content:center}
.nav{left:0;top:30px;width:1200px;height:95px;background:#fff}
.logo{display:flex;align-items:center;gap:10px}
.logo-mark{width:40px;height:40px;border-radius:50%;border:3px solid var(--olive)}
.logo-name{font-family:"Kalam",cursive;font-weight:700;font-size:26px;color:var(--olive)}
.nav-links{left:515px;top:38px;display:flex;gap:32px;font-size:14px;font-weight:600}
.nav-icon{top:30px;width:28px;height:28px;border-radius:50%}
.section-title{position:absolute;left:0;width:1200px;text-align:center;font-size:46px}
.section-title span{color:var(--rust)}
.benefit{position:absolute;width:240px;text-align:center;color:#fff}
.benefit .ring{width:104px;height:104px;border-radius:50%;margin:0 auto;border:5px solid #fff;box-shadow:0 0 0 3px rgba(255,255,255,.4)}
.benefit h3{font-size:22px;font-weight:500;margin-top:14px;letter-spacing:.5px;white-space:nowrap}
.benefit p{font-size:14px;line-height:24px;margin-top:14px;color:#f2f8ee}
.product{position:absolute;width:268px;text-align:center}
.product .shot{height:289px;position:relative}
.product h3{font-family:"Kalam",cursive;font-weight:700;font-size:34px;color:var(--rust);letter-spacing:3px;margin-top:14px;line-height:1}
.product p{font-size:13px;font-weight:500;margin-top:6px}
.product .btn{position:relative;margin:18px auto 0;width:160px;height:52px}
.cart-dot{width:28px;height:28px;border-radius:50%;border:2px solid #fff;display:inline-block}
.arrow-btn{position:absolute;width:42px;height:42px;border-radius:50%;border:2px solid var(--olive);display:flex;align-items:center;justify-content:center}
.review{position:absolute;width:258px;height:360px;background:#fff;box-shadow:0 6px 24px rgba(0,0,0,.07);padding:78px 20px 0}
.review .q{position:absolute;top:-28px;left:50%;margin-left:-36px;width:72px;height:72px;border-radius:50%;background:var(--olive);border:6px solid #fff;box-shadow:0 0 0 2px var(--olive)}
.review h4{font-family:"Kalam",cursive;font-weight:700;font-size:16px;color:#244e85;margin-top:-16px}
.review p{font-size:12.5px;line-height:22px;color:var(--muted);margin-top:12px}
.review .who{font-family:"Kalam",cursive;font-weight:700;color:#a8581f;font-size:18px;margin-top:14px}
.review .date{font-size:10px;color:var(--muted)}
.review .stars{position:absolute;right:20px;bottom:38px;color:#f5b400;font-size:17px;letter-spacing:2px}
.review.faded{opacity:.35}
.review.faded .q{background:#d0d0d0;box-shadow:0 0 0 2px #d0d0d0}
.post{position:absolute;left:650px;width:340px}
.post .date{font-size:11px;color:var(--ink)}
.post h3{font-family:"Kalam",cursive;font-weight:700;font-size:22px;line-height:26px;margin-top:8px}
.post p{font-size:13px;line-height:22px;margin-top:14px}
.post a{display:block;margin-top:14px;font-family:"Kalam",cursive;font-weight:700;color:var(--rust);font-size:15px;text-decoration:none}
.footer-col{position:absolute;top:4140px;color:#e9ebe5;font-size:12.5px}
.footer-col h5{font-family:"Kalam",cursive;font-weight:700;font-size:16px;color:#fff;margin-bottom:16px}
.footer-col li{list-style:none;line-height:31px}
.social{width:28px;height:28px;border-radius:50%;border:1.5px solid #fff;color:#fff;font-size:11px;display:flex;align-items:center;justify-content:center}
</style>
</head>
<body>

<div class="abs topbar">Get 20% Off Your First Purchase!</div>
<header class="abs nav">
  <div class="abs logo" style="left:120px;top:28px"><span class="logo-mark"></span><span class="logo-name">Pipkin</span></div>
  <nav class="abs nav-links"><span>Home</span><span>About Us</span><span>Products</span><span>Blog</span><span>Contact</span></nav>
  <span class="abs nav-icon" style="left:1044px;background:#f7b24a"></span>
  <span class="abs nav-icon" style="left:1082px;background:var(--olive)"></span>
</header>

<!-- Hero -->
<section>
  <svg class="abs" style="left:0;top:125px" width="1200" height="480" viewBox="0 0 1200 480">
    <path d="M0 0H1200V380C1000 420 850 400 700 440C520 490 250 420 0 465Z" fill="var(--beige)"/>
  </svg>
  <div class="media" role="img" aria-label="Photo of a smiling baby in a high chair holding a bowl and spoon" style="left:680px;top:125px;width:520px;height:440px;background:radial-gradient(circle at 55% 40%,#f3e6d7 0,#e9d2b8 45%,#c7d08b 85%);border-radius:0 0 0 60px"></div>
  <div class="media" role="img" aria-label="Formula pouch product rendering" style="left:575px;top:340px;width:180px;height:275px;border-radius:20px 20px 26px 26px;background:linear-gradient(#f7f7f2 0 38%,#8fb33c 48%,#7ca22a)"></div>
  <h1 class="abs display" style="left:156px;top:225px;font-size:84px">Perfect<br>Baby <span style="color:var(--rust)">Feed</span></h1>
  <a class="btn" style="left:156px;top:422px;width:118px;height:45px">Shop Now</a>
</section>

<!-- Who we are -->
<section>
  <svg class="abs" style="left:190px;top:645px" width="360" height="360" viewBox="0 0 360 360">
    <rect x="62" y="8" width="240" height="300" rx="10" fill="var(--olive)" transform="rotate(-8 180 160)"/>
    <rect x="50" y="30" width="270" height="300" rx="6" fill="none" stroke="var(--rust)" stroke-width="4" transform="rotate(10 180 180)"/>
  </svg>
  <div class="media" role="img" aria-label="Photo of a toddler sitting on a rug holding a formula pouch" style="left:228px;top:677px;width:281px;height:285px;border-radius:6px;background:linear-gradient(#8b8a86 0 55%,#e9e5dc 55%)"></div>
  <div class="media" role="img" aria-label="Line drawing of bananas" style="left:1040px;top:625px;width:140px;height:120px;border-radius:60px;background:#eef3d8"></div>
  <h2 class="abs display" style="left:652px;top:740px;font-size:44px">Who We Are</h2>
  <span class="underline" style="left:640px;top:803px"></span>
  <p class="abs" style="left:652px;top:820px;width:320px;font-size:14px;line-height:24px">Innovators in baby feeding solutions, dedicated to making parenting easier with our patented disposable formula pouches.</p>
  <a class="btn btn-outline" style="left:650px;top:922px;width:125px;height:42px">Read More</a>
</section>

<!-- Benefits -->
<section>
  <svg class="abs" style="left:0;top:1040px" width="1200" height="530" viewBox="0 0 1200 530">
    <path d="M0 15C200 40 350 50 600 30C850 10 1000 0 1200 20V520C1000 470 800 480 600 500C400 520 200 500 0 470Z" fill="var(--leaf)"/>
  </svg>
  <div class="media" role="img" aria-label="Dotted decorative pattern" style="left:1050px;top:1040px;width:150px;height:180px;border-radius:50%;background:rgba(255,255,255,.18)"></div>
  <h2 class="section-title display" style="top:1118px;color:#fff">Benefits</h2>
  <span class="underline" style="left:565px;top:1183px;background:#fff"></span>
  <svg class="abs" style="left:360px;top:1205px" width="480" height="90" viewBox="0 0 480 90">
    <path d="M10 30C60 0 120 0 160 50" fill="none" stroke="#fff" stroke-width="2" stroke-dasharray="7 6"/>
    <path d="M154 42L162 52L150 52" fill="none" stroke="#fff" stroke-width="2"/>
    <path d="M310 75C360 90 410 80 440 50" fill="none" stroke="#fff" stroke-width="2" stroke-dasharray="7 6"/>
    <path d="M432 50L442 48L440 58" fill="none" stroke="#fff" stroke-width="2"/>
  </svg>
  <div class="benefit" style="left:182px;top:1183px"><div class="ring" style="background:#fbedc1"></div><h3>EASY TO USE</h3><p>Our pouches are designed for convenience – just squeeze, shake, and feed.</p></div>
  <div class="benefit" style="left:480px;top:1213px"><div class="ring" style="background:#dff3f4"></div><h3>SAFE AND HYGIENIC</h3><p>Each pouch ensures a fresh, uncontaminated meal for your baby every time.</p></div>
  <div class="benefit" style="left:778px;top:1183px"><div class="ring" style="background:#fbe8d8"></div><h3>TRAVEL FRIENDLY</h3><p>Compact and portable, perfect for feeding on the go.</p></div>
  <div class="media" role="img" aria-label="Drawing of an eggplant" style="left:15px;top:1470px;width:160px;height:150px;border-radius:50% 40% 50% 50%;background:#f08a84;transform:rotate(-35deg)"></div>
</section>

<!-- Products -->
<section>
  <h2 class="section-title display" style="top:1590px"><span>Our</span> Products</h2>
  <span class="underline" style="left:565px;top:1648px"></span>
  <div class="arrow-btn" style="left:83px;top:1827px"><svg width="14" height="14" viewBox="0 0 14 14"><path d="M9 2L4 7L9 12" fill="none" stroke="#333" stroke-width="1.8"/></svg></div>
  <div class="arrow-btn" style="left:1054px;top:1827px"><svg width="14" height="14" viewBox="0 0 14 14"><path d="M5 2L10 7L5 12" fill="none" stroke="#333" stroke-width="1.8"/></svg></div>

  <div class="product" style="left:158px;top:1683px">
    <div class="shot" role="img" aria-label="QuickMix formula pouch on a peach background" style="background:linear-gradient(#ffe3d8 0 68%,#ffc9a8 68%)"></div>
    <h3>QuickMix</h3><p>Formula Pouch</p>
    <a class="btn">Add to Cart <span class="cart-dot"></span></a>
  </div>
  <div class="product" style="left:451px;top:1683px">
    <div class="shot" role="img" aria-label="CalmBlend formula canister on a green background" style="background:linear-gradient(#e3fbd6 0 68%,#acdc8f 68%)"></div>
    <h3>CalmBlend</h3><p>Formula Canister</p>
    <a class="btn">Add to Cart <span class="cart-dot"></span></a>
  </div>
  <div class="product" style="left:744px;top:1683px">
    <div class="shot" role="img" aria-label="RoamFeed starter kit on a yellow background" style="background:linear-gradient(#fdf9d8 0 68%,#f3eeb0 68%)"></div>
    <h3>RoamFeed</h3><p>Starter Kit</p>
    <a class="btn">Add to Cart <span class="cart-dot"></span></a>
  </div>
  <div class="media" role="img" aria-label="Line drawing of broccoli" style="left:1010px;top:2148px;width:105px;height:100px;border-radius:50%;background:#eef5e4"></div>
</section>

<!-- Promo -->
<section>
  <svg class="abs" style="left:0;top:2215px" width="1200" height="560" viewBox="0 0 1200 560">
    <path d="M0 40C250 20 400 60 650 55C900 50 1050 0 1200 10V510C1000 520 800 490 600 505C400 520 200 545 0 545Z" fill="var(--beige)"/>
  </svg>
  <div class="media" role="img" aria-label="Photo of a baby in a high chair holding an orange bowl" style="left:620px;top:2265px;width:580px;height:440px;border-radius:120px 0 0 0;background:radial-gradient(circle at 35% 50%,#f6cf9a 0,#e9d7b6 40%,#c9cdbf 80%)"></div>
  <h2 class="abs display" style="left:135px;top:2380px;font-size:44px;line-height:54px;color:var(--rust);font-weight:700">Experience the convenience<br>of our disposable baby<br>formula <span style="color:var(--olive)">pouches today</span><span style="color:var(--ink)">!</span></h2>
  <a class="btn" style="left:135px;top:2569px;width:120px;height:44px">Shop Now</a>
</section>

<!-- Testimonials -->
<section>
  <h2 class="section-title display" style="top:2833px">Our Clients <span>Say</span></h2>
  <span class="underline" style="left:565px;top:2892px"></span>
  <div class="review faded" style="left:-110px;top:2939px"><span class="q"></span><h4>Lorem ipsum dolor</h4><p>Lorem ipsum dolor sit amet consectetur. Varius purus elit dolor fusce donec aliquam vulputate purus. Convallis sed vitae fames ut quam est a lobortis pellentesque. Nec diam et et nibh tempor erat tellus.</p><div class="who">JOHN DOE</div><div class="date">11 May 2024</div><div class="stars">★★★★★</div></div>
  <div class="review" style="left:188px;top:2939px"><span class="q"></span><h4>Lorem ipsum dolor</h4><p>Lorem ipsum dolor sit amet consectetur. Varius purus elit dolor fusce donec aliquam vulputate purus. Convallis sed vitae fames ut quam est a lobortis pellentesque. Nec diam et et nibh tempor erat tellus.</p><div class="who">JOHN DOE</div><div class="date">11 May 2024</div><div class="stars">★★★★★</div></div>
  <div class="review" style="left:471px;top:2939px"><span class="q"></span><h4>Lorem ipsum dolor</h4><p>Lorem ipsum dolor sit amet consectetur. Varius purus elit dolor fusce donec aliquam vulputate purus. Convallis sed vitae fames ut quam est a lobortis pellentesque. Nec diam et et nibh tempor erat tellus.</p><div class="who">JOHN DOE</div><div class="date">11 May 2024</div><div class="stars">★★★★★</div></div>
  <div class="review" style="left:755px;top:2939px"><span class="q"></span><h4>Lorem ipsum dolor</h4><p>Lorem ipsum dolor sit amet consectetur. Varius purus elit dolor fusce donec aliquam vulputate purus. Convallis sed vitae fames ut quam est a lobortis pellentesque. Nec diam et et nibh tempor erat tellus.</p><div class="who">JOHN DOE</div><div class="date">11 May 2024</div><div class="stars">★★★★★</div></div>
  <div class="review faded" style="left:1038px;top:2939px"><span class="q"></span><h4>Lorem ipsum dolor</h4><p>Lorem ipsum dolor sit amet consectetur. Varius purus elit dolor fusce donec aliquam vulputate purus. Convallis sed vitae fames ut quam est a lobortis pellentesque. Nec diam et et nibh tempor erat tellus.</p><div class="who">JOHN DOE</div><div class="date">11 May 2024</div><div class="stars">★★★★★</div></div>
  <svg class="abs" style="left:145px;top:3100px" width="20" height="34" viewBox="0 0 20 34"><path d="M16 3L4 17L16 31" fill="none" stroke="var(--olive)" stroke-width="4"/></svg>
  <svg class="abs" style="left:1046px;top:3100px" width="20" height="34" viewBox="0 0 20 34"><path d="M4 3L16 17L4 31" fill="none" stroke="var(--olive)" stroke-width="4"/></svg>
</section>

<!-- Blog -->
<section>
  <h2 class="section-title display" style="top:3392px"><span>Our</span> Blog</h2>
  <span class="underline" style="left:565px;top:3450px"></span>
  <div class="abs" style="left:158px;top:3500px;width:884px;height:460px;border-radius:40px;background:var(--cream)"></div>
  <div class="media" role="img" aria-label="Formula pouch on a green wavy background" style="left:158px;top:3500px;width:441px;height:460px;border-radius:40px 0 0 40px;background:var(--leaf)"></div>
  <div class="media" role="img" aria-label="Line drawing of an onion" style="left:100px;top:3840px;width:95px;height:150px;border-radius:50%;background:#fff2a8;opacity:.8"></div>
  <article class="post" style="top:3545px"><div class="date">▢ 07 June 2024</div><h3>Innovative Feeding<br>Solutions</h3><p>Discover how our patented pouches are changing the baby formula industry.</p><a>Read More &nbsp;→</a></article>
  <div class="abs" style="left:600px;top:3760px;width:442px;height:2px;background:#fff"></div>
  <article class="post" style="top:3775px"><div class="date">▢ 07 June 2024</div><h3>Tips for New Parents</h3><p>Helpful advice and tips to make your parenting journey smoother.</p><a>Read More &nbsp;→</a></article>
</section>

<!-- Footer -->
<footer>
  <svg class="abs" style="left:0;top:4040px" width="1200" height="436" viewBox="0 0 1200 436"><path d="M0 30C300 70 600 60 900 20C1050 0 1130 5 1200 15V436H0Z" fill="var(--footer)"/></svg>
  <div class="abs logo" style="left:160px;top:4168px"><span class="logo-mark" style="border-color:#fff"></span><span class="logo-name" style="color:#fff">Pipkin</span></div>
  <div class="abs" style="left:140px;top:4271px;display:flex;gap:10px"><span class="social">f</span><span class="social">◎</span><span class="social">X</span><span class="social">in</span></div>
  <div class="footer-col" style="left:425px"><h5>Shop</h5><ul><li>QuickMix</li><li>CalmBlend</li><li>RoamFeed</li><li>CalmBlend</li><li>RoamFeed</li></ul></div>
  <div class="footer-col" style="left:542px"><h5>Company</h5><ul><li>About</li><li>Careers</li><li>Blog</li><li>Reviews</li></ul></div>
  <div class="footer-col" style="left:667px"><h5>Legal</h5><ul><li>FAQ's</li><li>Privacy Policy</li><li>Support</li><li>Terms of Service</li></ul></div>
  <div class="footer-col" style="left:823px;width:235px"><h5 style="font-size:20px">Subscribe our newsletter</h5><p style="font-size:10.5px;line-height:15px;margin-top:-6px">Get the latest updates, offers, and tips. Join our community today!</p>
    <div style="margin-top:18px;border-bottom:1px solid #cfd2ca;padding-bottom:8px;display:flex;justify-content:space-between;font-size:12px"><span>Email</span><span style="color:var(--olive)">→</span></div></div>
  <p class="abs" style="left:0;top:4398px;width:1200px;text-align:center;color:#e9ebe5;font-size:12px">Copyright © 2024 | Pipkin</p>
</footer>

</body>
</html>
```